2024 Comprehensive Needs Assessment

Design our 2024 Binder Report Cover. Front, Spine, Back. We are in the Education field, reporting data for strategic planning. I have attached our color palette and the previous years covers as a sample.

```html
<!DOCTYPE html>
<html lang="en">
<head>
<meta charset="utf-8">
<title>2024 Comprehensive Needs Assessment – Binder Cover</title>
<link rel="stylesheet" href="https://fonts.googleapis.com/css2?family=Oswald:wght@500;600&family=Montserrat:wght@400;600;700;800&family=EB+Garamond:wght@500&display=swap">
<style>
  :root {
    --page: #ffffff;
    --back-bg: #23262e;
    --ink: #0a3a44;
    --blue: #03627c;
    --teal: #00c4b4;
    --white: #ffffff;
    --district-ink: #0b4a5a;
    --photo-light: #d9d8d2;
    --photo-warm: #c9a57c;
  }
  * { margin: 0; padding: 0; box-sizing: border-box; }
  html, body { width: 960px; height: 1200px; overflow: hidden; background: var(--page); }
  .canvas { position: relative; width: 960px; height: 1200px; }
  .spread {
    position: absolute; left: 30px; top: 280px;
    width: 924px; height: 658px;
    transform: scale(0.974); transform-origin: top left;
    display: flex;
  }
  .back-cover { position: relative; width: 430px; height: 658px; background: var(--back-bg); color: var(--white); }
  .spine { position: relative; width: 63px; height: 658px; background: var(--ink); border-left: 1px solid #31535b; overflow: hidden; }
  .front-cover { position: relative; width: 431px; height: 658px; background: var(--ink); overflow: hidden; }

  .title-stack { position: absolute; text-align: center; line-height: 1; }
  .title-line { font-family: "Oswald", sans-serif; font-weight: 600; color: var(--white); letter-spacing: 0.2px; }
  .title-key { font-family: "Montserrat", sans-serif; font-weight: 800; color: var(--teal); letter-spacing: 1px; }

  .back-cover .title-stack { left: 0; width: 430px; top: 68px; }
  .back-cover .title-line.top { font-size: 24px; }
  .back-cover .title-key { font-size: 40px; margin: 2px 0 1px; }
  .back-cover .title-line.bottom { font-size: 29px; }

  .summary-heading { position: absolute; top: 212px; left: 0; width: 430px; text-align: center; font-family: "EB Garamond", serif; font-weight: 500; font-size: 18px; letter-spacing: 0.5px; }
  .summary-body { position: absolute; top: 238px; left: 28px; width: 375px; font-family: "Montserrat", sans-serif; font-size: 13.3px; line-height: 18px; text-align: justify; }

  .brand { position: absolute; display: flex; align-items: center; gap: 6px; font-family: "Montserrat", sans-serif; font-weight: 700; color: var(--white); line-height: 1.05; }
  .brand-dot { flex: none; border-radius: 50%; background: var(--teal); }
  .back-cover .brand { left: 55px; top: 568px; font-size: 15px; }
  .back-cover .brand-dot { width: 14px; height: 14px; }
  .contact { position: absolute; left: 190px; top: 573px; width: 190px; text-align: center; font-family: "Montserrat", sans-serif; font-weight: 700; font-size: 12.5px; line-height: 16px; font-style: normal; }

  .spine .brand { left: 6px; top: 28px; font-size: 7px; gap: 3px; }
  .spine .brand-dot { width: 6px; height: 6px; }
  .spine-title { position: absolute; left: 18px; top: 97px; writing-mode: vertical-rl; font-family: "Oswald", sans-serif; font-weight: 600; font-size: 22px; color: var(--white); white-space: nowrap; line-height: 1; }
  .spine-title .title-key { font-family: "Oswald", sans-serif; font-weight: 600; letter-spacing: 0; }
  .spine-district { position: absolute; left: 14px; top: 458px; writing-mode: vertical-rl; line-height: 1; white-space: nowrap; }
  .spine-district .district-name { display: block; font-family: "Montserrat", sans-serif; font-weight: 700; font-size: 20px; color: var(--teal); letter-spacing: 1.5px; }
  .spine-district .district-type { display: block; font-family: "Montserrat", sans-serif; font-weight: 700; font-size: 11px; color: var(--white); margin-left: 2px; }
  .spine-year { position: absolute; left: 0; width: 63px; top: 598px; text-align: center; font-family: "Oswald", sans-serif; font-weight: 600; font-size: 21px; line-height: 1; color: var(--teal); }

  .cover-art { position: absolute; inset: 0; width: 431px; height: 658px; }
  .front-cover .brand { left: 28px; top: 48px; font-size: 24px; }
  .front-cover .brand-dot { width: 22px; height: 22px; }
  .front-cover .title-stack { left: 90px; width: 230px; top: 418px; }
  .front-cover .title-line.top { font-size: 23px; }
  .front-cover .title-key { font-size: 38px; margin: 1px 0 0; }
  .front-cover .title-line.bottom { font-size: 28px; }
  .district { position: absolute; left: 70px; top: 522px; line-height: 1; }
  .district .district-name { display: block; font-family: "Montserrat", sans-serif; font-weight: 700; font-size: 33px; color: var(--teal); letter-spacing: 1.5px; }
  .district .district-type { display: block; font-family: "Montserrat", sans-serif; font-weight: 700; font-size: 18px; color: var(--district-ink); letter-spacing: 1px; margin-top: 3px; }
  .cover-year { position: absolute; left: 292px; top: 528px; font-family: "Oswald", sans-serif; font-weight: 600; font-size: 48px; line-height: 1; color: var(--blue); }
</style>
</head>
<body>
<div class="canvas">
  <div class="spread">
    <section class="back-cover">
      <div class="title-stack">
        <div class="title-line top">COMPREHENSIVE</div>
        <div class="title-key">NEEDS</div>
        <div class="title-line bottom">ASSESSMENT</div>
      </div>
      <h2 class="summary-heading">SUMMARY</h2>
      <p class="summary-body">Lorem ipsum dolor sit amet, consectetur adipiscing elit, sed do eiusmod tempor incididunt ut labore et dolore magna aliqua. Ut enim ad minim veniam, quis nostrud exercitation ullamco laboris nisi ut aliquip ex ea commodo consequat. Duis aute irure dolor in reprehenderit in voluptate velit esse cillum dolore eu fugiat nulla pariatur. Excepteur sint occaecat cupidatat non proident, sunt in culpa qui officia deserunt mollit anim id est laborum.</p>
      <div class="brand"><span class="brand-dot"></span><span>Learning<br>Bridge, LLC</span></div>
      <address class="contact">4120 Harrow Mill Lane<br>Brookfield, MS 38620<br>662-555-0148</address>
    </section>

    <section class="spine">
      <div class="brand"><span class="brand-dot"></span><span>Learning<br>Bridge</span></div>
      <div class="spine-title">COMPREHENSIVE <span class="title-key">NEEDS</span> ASSESSMENT</div>
      <div class="spine-district"><span class="district-name">RIVERTON</span><span class="district-type">SCHOOL DISTRICT</span></div>
      <div class="spine-year">2024</div>
    </section>

    <section class="front-cover">
      <svg class="cover-art" viewBox="0 0 431 658" xmlns="http://www.w3.org/2000/svg">
        <defs>
          <linearGradient id="photo-tone" x1="0" y1="0" x2="1" y2="1">
            <stop offset="0" stop-color="#c9a57c"/>
            <stop offset="0.35" stop-color="#d9d8d2"/>
            <stop offset="0.8" stop-color="#cfcdc7"/>
            <stop offset="1" stop-color="#b99770"/>
          </linearGradient>
        </defs>
        <polygon class="blue-band" points="232,0 300,0 0,470 0,380" fill="#03627c"/>
        <polygon class="cover-photo" role="img" aria-label="Photo of a hand holding a pen over printed charts and reports on a wooden desk" points="300,0 431,0 431,320 210,658 0,658 0,470" fill="url(#photo-tone)"/>
        <polygon class="teal-stripe" points="250,110 282,110 0,540 0,492" fill="#00c4b4"/>
        <polygon class="title-shade" points="112,412 350,412 280,519 42,519" fill="#1a3440" opacity="0.35"/>
        <polygon class="blue-stripe" points="431,300 431,380 248,658 228,658" fill="#03627c"/>
        <polygon class="teal-corner" points="431,390 431,658 252,658" fill="#00c4b4"/>
        <polygon class="district-band" points="30,519 330,519 302,585 0,585" fill="#ffffff"/>
      </svg>
      <div class="brand"><span class="brand-dot"></span><span>Learning<br>Bridge</span></div>
      <div class="title-stack">
        <div class="title-line top">COMPREHENSIVE</div>
        <div class="title-key">NEEDS</div>
        <div class="title-line bottom">ASSESSMENT</div>
      </div>
      <div class="district"><span class="district-name">RIVERTON</span><span class="district-type">SCHOOL DISTRICT</span></div>
      <div class="cover-year">2024</div>
    </section>
  </div>
</div>
</body>
</html>
```